Essential oil label for bottles

Looking to modify our current logo and label design. It looks too simple. I will attach images of our competitors to use as examples. Our company name is Velnora. We have 2 different bottles. Clear and amber color. Going forward, we will be using only the amber bottle. The other 2 images are the biggest sellers brands. We want to make some adjustments to ours.

Target Market(s)

Brindex sales

Industry/Entity Type

Essential oil, perfume

Colors

Designer to choose only greyscale colors for use in the design.

Requirements
Nice to have
• A slight change to fonts and logo design. Maybe change the font and design of the word "Velnora" in our logo. Maybe add something to the label to make it stand out more but still keeping it clean and modern
Should not have
• No colors, besides, black, grays, whites, and off white.

```html
<!DOCTYPE html>
<html lang="en">
<head>
<meta charset="utf-8">
<title>Velnora – White Tea Fragrance Oil Labels</title>
<link rel="stylesheet" href="https://fonts.googleapis.com/css2?family=Archivo:wdth,wght@62..125,300..800&display=swap">
<style>
  :root {
    --page-bg: #efeeec;
    --label-dark: #242424;
    --label-dark-edge: #1c1c1c;
    --label-light: #f2f2f2;
    --label-light-edge: #d6d6d6;
    --ink-light: #f4f4f4;
    --ink-dark: #1e1e1e;
    --ink-muted-dark: #4a4a4a;
    --ink-muted-light: #cfcfcf;
    --rule-dark: #5a5a5a;
    --rule-light: #6a6a6a;
  }
  * { box-sizing: border-box; margin: 0; padding: 0; }
  html, body {
    width: 1200px;
    height: 800px;
    overflow: hidden;
    background: var(--page-bg);
    font-family: "Archivo", Arial, sans-serif;
  }
  .canvas {
    position: relative;
    width: 1200px;
    height: 800px;
  }
  .label {
    position: absolute;
    top: 122px;
    width: 400px;
    height: 555px;
    box-shadow: 0 10px 30px rgba(0,0,0,0.08);
  }
  .label--dark {
    left: 170px;
    background: linear-gradient(90deg, var(--label-dark-edge), var(--label-dark) 40%, var(--label-dark-edge));
    color: var(--ink-light);
  }
  .label--light {
    left: 630px;
    background: linear-gradient(90deg, #fafafa, var(--label-light) 45%, var(--label-light-edge));
    color: var(--ink-dark);
  }
  .brand {
    position: absolute;
    left: 65px;
    top: 42px;
    display: flex;
    align-items: center;
    gap: 16px;
  }
  .brand__dot {
    width: 22px;
    height: 22px;
    border-radius: 50%;
    border: 1.5px solid currentColor;
  }
  .brand__name {
    font-weight: 300;
    font-stretch: 125%;
    font-size: 18px;
    letter-spacing: 0.62em;
  }
  .product-name {
    position: absolute;
    left: 65px;
    top: 138px;
    font-weight: 700;
    font-stretch: 125%;
    font-size: 26px;
    letter-spacing: 0.02em;
  }
  .product-type {
    position: absolute;
    left: 65px;
    top: 261px;
    font-weight: 400;
    font-stretch: 110%;
    font-size: 15px;
    letter-spacing: 0.02em;
  }
  .product-rule {
    position: absolute;
    left: 65px;
    top: 292px;
    width: 262px;
    height: 1px;
  }
  .label--dark .product-rule { background: var(--rule-dark); }
  .label--light .product-rule { background: var(--rule-light); }
  .notes {
    position: absolute;
    left: 65px;
    top: 305px;
    display: flex;
    align-items: center;
    font-size: 13px;
    font-stretch: 105%;
    letter-spacing: 0.02em;
    white-space: nowrap;
  }
  .notes__item { padding: 0 4px; line-height: 18px; }
  .notes__item + .notes__item { border-left: 1px solid currentColor; line-height: 14px; }
  .notes__item--key { padding: 1px 4px; }
  .label--dark .notes__item--key { background: var(--ink-muted-light); color: var(--label-light); }
  .label--light .notes__item--key { background: var(--ink-dark); color: var(--ink-light); }
  .volume {
    position: absolute;
    left: 65px;
    top: 501px;
    font-size: 14px;
    font-stretch: 105%;
  }
</style>
</head>
<body>
  <main class="canvas">
    <section class="label label--dark" aria-label="Velnora White Tea label, black edition">
      <div class="brand">
        <span class="brand__dot"></span>
        <span class="brand__name">VELNORA</span>
      </div>
      <h1 class="product-name">WHITETEA</h1>
      <p class="product-type">FRAGRANCE OIL</p>
      <div class="product-rule"></div>
      <p class="notes">
        <span class="notes__item notes__item--key">WHITETEA</span>
        <span class="notes__item">ORANGE</span>
        <span class="notes__item">PALOSANTO</span>
      </p>
      <p class="volume">200 ML</p>
    </section>

    <section class="label label--light" aria-label="Velnora White Tea label, white edition">
      <div class="brand">
        <span class="brand__dot"></span>
        <span class="brand__name">VELNORA</span>
      </div>
      <h2 class="product-name">WHITETEA</h2>
      <p class="product-type">FRAGRANCE OIL</p>
      <div class="product-rule"></div>
      <p class="notes">
        <span class="notes__item notes__item--key">WHITETEA</span>
        <span class="notes__item">ORANGE</span>
        <span class="notes__item">PALOSANTO</span>
      </p>
      <p class="volume">200 ML</p>
    </section>
  </main>
</body>
</html>
```